Website for AV installation with booking system and e-commerce

Company: Velqora
Tag Line: Audio Visual and Security System Installations
We need a website for an AV company based in Sydney Australia. We specialise in Audio Visual, CCTV (security cameras), and Data Cabling.
The purpose of the website is that customers book their installation online with a live booking system.
We are looking for the following:
- Creative and modern design
- easy to use - keep in mind that the user who will book will have little knowledge in technology.
- clean and organised
- colours to work in well with our logo we also like royal to navy blue, but we are open to other suggested what works well with our logo.
We want customers to be able to add products needed for their installation ie when booking to wall mount their TV they can choose to add a TV bracket and cables to the cart and vise-versa buy a bracket or cables and add to cart the installation.
Tabs to be included:
About us
Gallery
Contact Us
Home
Services (there are three services that we offer - Residential, Corporate and Retail)
Products
Book Online/Cart (checkout)
Temporary website checkout: www.velqora.com.au, please note this is very basic and we do not want a copy of this. This is purely to give you an idea of our company.
Good Luck!
Updates
Target Market(s)
home owners/renters, business owners, archiects/designers, builders
Industry/Entity Type
E-Commerce
Look and feel

```html
<!DOCTYPE html>
<html lang="en">
<head>
<meta charset="utf-8">
<title>Velqora – Audio Visual and Security System Installations</title>
<link rel="stylesheet" href="https://fonts.googleapis.com/css2?family=Oswald:wght@300;400;500;600&family=Lexend+Zetta:wght@300;800;900&family=Arimo:wght@400;700&display=swap">
<style>
  :root {
    --red: #e8000b;
    --red-dark: #b9000a;
    --ink: #2b2b2b;
    --body: #333333;
    --white: #ffffff;
    --sky: #5d9fd6;
  }
  * { box-sizing: border-box; margin: 0; padding: 0; }
  html, body { width: 784px; height: 1200px; overflow: hidden; background: var(--white); }
  body { position: relative; font-family: "Arimo", Arial, sans-serif; color: var(--body); }
  a { color: inherit; text-decoration: none; }

  .site-header { position: absolute; left: 0; top: 0; width: 784px; height: 90px; background: var(--white); }
  .brand { position: absolute; left: 32px; top: 22px; display: flex; align-items: center; gap: 10px; }
  .brand-dot { width: 18px; height: 18px; border-radius: 50%; background: var(--red); }
  .brand-name { font-family: "Oswald", sans-serif; font-weight: 600; font-size: 40px; line-height: 1; color: var(--red); letter-spacing: 1px; }

  .main-nav { position: absolute; left: 0; top: 90px; width: 784px; height: 36px; background: linear-gradient(#f2000c, var(--red-dark)); }
  .main-nav ul { list-style: none; display: flex; align-items: center; height: 36px; padding-left: 26px; gap: 15px; }
  .main-nav li { font-family: "Oswald", sans-serif; font-weight: 300; font-size: 15.5px; color: var(--white); letter-spacing: -0.3px; }
  .nav-home { margin-right: 2px; }
  .nav-home svg { display: block; }

  .book-cta { position: absolute; left: 464px; top: 0; width: 247px; height: 120px; border-radius: 0 0 6px 6px;
    background: linear-gradient(#ffffff, #d8d8d8); box-shadow: 0 2px 6px rgba(0,0,0,.35); text-align: center; z-index: 2; }
  .book-cta-title { font-family: "Oswald", sans-serif; font-weight: 600; font-size: 23px; color: var(--red); margin-top: 22px; letter-spacing: -0.3px; }
  .book-cta-text { font-family: "Oswald", sans-serif; font-weight: 500; font-size: 13px; line-height: 17px; color: #3a3a3a; margin-top: 10px; }

  .hero { position: absolute; left: 0; top: 126px; width: 784px; height: 356px;
    background:
      radial-gradient(ellipse 150px 130px at 90px 60px, rgba(225,225,225,.95), rgba(225,225,225,0) 100%),
      radial-gradient(ellipse 110px 190px at 690px 110px, rgba(230,230,230,.95), rgba(230,230,230,0) 100%),
      radial-gradient(ellipse 200px 150px at 540px 330px, rgba(215,215,215,.95), rgba(215,215,215,0) 100%),
      linear-gradient(100deg, #1f6cb5 0%, #3e8cd0 30%, #7fb4e2 50%, #d9e9f6 70%, #a9cdee 100%); }

  .tagline-band { position: absolute; left: 0; top: 482px; width: 784px; height: 136px; background: var(--red); }
  .tagline { position: absolute; left: 30px; top: 497px; font-family: "Lexend Zetta", sans-serif; font-size: 22.5px; color: var(--white);
    letter-spacing: -3.2px; white-space: nowrap; text-shadow: 0 1px 2px rgba(0,0,0,.3); }
  .tagline strong { font-weight: 800; }
  .tagline span { font-weight: 300; }

  .footer-band { position: absolute; left: 0; top: 1102px; width: 784px; height: 98px; background: var(--red); }

  .content-panel { position: absolute; left: 16px; top: 546px; width: 754px; height: 608px; border-radius: 6px;
    background: linear-gradient(#d9d9d9 0%, #ffffff 22%, #ffffff 85%, #d6d6d6 100%);
    box-shadow: 0 0 0 2px var(--red-dark), 0 2px 8px rgba(0,0,0,.4); }

  .intro-title { position: absolute; left: 53px; top: 583px; font-family: "Oswald", sans-serif; font-weight: 500; font-size: 22px; color: var(--ink); letter-spacing: -0.5px; }
  .intro-title em { font-style: normal; color: var(--red); }
  .intro-sub { position: absolute; left: 64px; top: 612px; font-family: "Oswald", sans-serif; font-weight: 300; font-size: 14.5px; color: #3a3a3a; }
  .product-visual { position: absolute; left: 70px; top: 658px; width: 234px; height: 182px; border-radius: 4px;
    background: linear-gradient(160deg, #4a4a4a, #1f1f1f 55%, #bdbdbd); }
  .intro-copy { position: absolute; left: 50px; top: 870px; width: 314px; font-size: 11px; line-height: 13.5px; color: var(--body); }
  .btn-request { position: absolute; left: 50px; top: 994px; width: 167px; height: 30px; border-radius: 4px;
    background: linear-gradient(#ff1a22, var(--red-dark)); box-shadow: 0 0 0 2px #fff, 0 0 0 3px var(--red-dark);
    color: var(--white); font-weight: 700; font-size: 10.5px; line-height: 30px; text-align: center; }

  .service { position: absolute; left: 418px; width: 340px; }
  .service-icon { position: absolute; left: 0; top: 0; width: 58px; height: 58px; }
  .service-name { position: absolute; left: 79px; top: -6px; font-family: "Lexend Zetta", sans-serif; font-weight: 900; font-size: 18.5px;
    color: var(--red); letter-spacing: -3.4px; }
  .service-copy { position: absolute; left: 79px; top: 18px; width: 260px; font-size: 9.6px; line-height: 11.6px; color: var(--body); }
  .service-pill { position: absolute; left: 78px; top: 82px; width: 211px; height: 21px; border-radius: 6px;
    background: linear-gradient(#aeaeae, #8a8a8a); color: var(--white); font-weight: 700; font-size: 9.6px; line-height: 21px; padding-left: 14px; }

  .site-footer { position: absolute; left: 0; top: 1160px; width: 784px; text-align: center; color: var(--white); }
  .footer-nav { font-size: 10.5px; }
  .footer-nav span { margin: 0 4px; }
  .copyright { font-size: 8.5px; margin-top: 6px; }
</style>
</head>
<body>
  <header class="site-header">
    <a class="brand" href="#"><span class="brand-dot"></span><span class="brand-name">Velqora</span></a>
  </header>

  <nav class="main-nav">
    <ul>
      <li class="nav-home"><svg width="20" height="18" viewBox="0 0 20 18"><path d="M10 1 1 9h3v8h4.5v-5h3v5H16V9h3z" fill="#fff"/></svg></li>
      <li>ABOUT US</li><li>SERVICES</li><li>PRODUCTS</li><li>GALLERY</li><li>CONTACT US</li>
    </ul>
  </nav>

  <a class="book-cta" href="#">
    <div class="book-cta-title">CLICK HERE BOOK NOW!</div>
    <div class="book-cta-text">I NEED AN AUDIO VISUAL AND<br>SECURITY SYSTEM INSTALLATION NOW</div>
  </a>

  <div class="hero" role="img" aria-label="Security cameras mounted in front of a glass office tower under a blue sky"></div>

  <div class="tagline-band"></div>
  <h1 class="tagline"><strong>Audio Visual and</strong> <span>Security System Installations</span></h1>
  <div class="footer-band"></div>

  <main class="content-panel"></main>

  <h2 class="intro-title">FIND PEACE OF MIND WITH <em>VELQORA</em></h2>
  <p class="intro-sub">We are committed in securing people and your premises.</p>
  <div class="product-visual" role="img" aria-label="CCTV monitoring screen showing camera feeds beside a desktop recorder tower"></div>
  <p class="intro-copy">Lorem ipsum dolor sit amet, consectetur adipisicing elit, sed do eiusmod tempor incididunt ut labore et dolore magna aliqua. Ut enim ad minim veniam, quis nostrud exercitation ullamco laboris nisi ut aliquip ex ea commodo consequat. Duis aute irure dolor in reprehenderit in voluptate velit esse cillum dolore eu fugiat nulla pariatur. Excepteur sint occaecat cupidatat non proident, sunt in culpa qui officia deserunt mollit anim id est laborum.</p>
  <a class="btn-request" href="#">REQUEST FOR INSTALLATION</a>

  <section class="service" style="top:607px">
    <svg class="service-icon" viewBox="0 0 58 58"><circle cx="29" cy="29" r="28" fill="var(--red)"/><circle cx="29" cy="29" r="23" fill="none" stroke="#fff" stroke-width="2.5"/><path d="M29 17 17 28h4v11h16V28h4z" fill="#fff"/><rect x="25" y="30" width="8" height="9" fill="var(--red)"/></svg>
    <h3 class="service-name">RESIDENTIAL</h3>
    <p class="service-copy">Lorem ipsum dolor sit amet, consectetur adipisicing elit, sed do eiusmod tempor incididunt ut labore et dolore magna aliqua. Ut enim ad minim veniam, quis nostrud exercitation ullamco laboris nisi ut aliquip ex ea commodo consequat.</p>
    <a class="service-pill" href="#">request for Residential installation now!</a>
  </section>

  <section class="service" style="top:751px">
    <svg class="service-icon" viewBox="0 0 58 58"><circle cx="29" cy="29" r="28" fill="var(--red)"/><circle cx="29" cy="29" r="23" fill="none" stroke="#fff" stroke-width="2.5"/><rect x="18" y="20" width="12" height="19" fill="#fff"/><rect x="31" y="16" width="10" height="23" fill="#fff"/><g fill="var(--red)"><rect x="21" y="23" width="2" height="2"/><rect x="25" y="23" width="2" height="2"/><rect x="21" y="28" width="2" height="2"/><rect x="25" y="28" width="2" height="2"/><rect x="33" y="20" width="6" height="1.5"/><rect x="33" y="24" width="6" height="1.5"/><rect x="33" y="28" width="6" height="1.5"/><rect x="33" y="32" width="6" height="1.5"/></g></svg>
    <h3 class="service-name">CORPORATE</h3>
    <p class="service-copy">Lorem ipsum dolor sit amet, consectetur adipisicing elit, sed do eiusmod tempor incididunt ut labore et dolore magna aliqua. Ut enim ad minim veniam, quis nostrud exercitation ullamco laboris nisi ut aliquip ex ea commodo consequat.</p>
    <a class="service-pill" href="#">request for Corporate installation now!</a>
  </section>

  <section class="service" style="top:903px">
    <svg class="service-icon" viewBox="0 0 58 58"><circle cx="29" cy="29" r="28" fill="var(--red)"/><circle cx="29" cy="29" r="23" fill="none" stroke="#fff" stroke-width="2.5"/><path d="M16 22 38 17l2 8-22 5z" fill="#fff"/><path d="M26 29l2 6h-6v5h-3V31h3z" fill="#fff"/><rect x="36" y="28" width="6" height="3" fill="#fff"/></svg>
    <h3 class="service-name">RETAIL</h3>
    <p class="service-copy">Lorem ipsum dolor sit amet, consectetur adipisicing elit, sed do eiusmod tempor incididunt ut labore et dolore magna aliqua. Ut enim ad minim veniam, quis nostrud exercitation ullamco laboris nisi ut aliquip ex ea commodo consequat.</p>
    <a class="service-pill" href="#">visit our Products section for retail</a>
  </section>

  <footer class="site-footer">
    <div class="footer-nav">ABOUT US<span>·</span>SERVICES<span>·</span>PRODUCTS<span>·</span>GALLERY<span>·</span>CONTACT US</div>
    <div class="copyright">© Copyright 2013 Velqora. All Rights Reserved</div>
  </footer>
</body>
</html>
```